Multi product banner ads

We need a set of creatives containing various products within the same banner ad. For instance, a piece containing a cable offer, an insurance offer and a flight offer, no matter the size: MPU, skyscraper or Leaderboard.
The creative must contain multiple click tags, be compatible with Flash 10 and AS2. We would like to see proposals that replicate text ads and proposals that contain images and that are animated. Once we pick a format, we would need further help replicating to other industries.

Requirements
Must have
• at least 3 spaces for products on any given slide.
• compatible with Flash 10 and AS2
• <50KB

```html
<!DOCTYPE html>
<html lang="en">
<head>
<meta charset="utf-8">
<title>Multi Product Banner – MPU States</title>
<link rel="stylesheet" href="https://fonts.googleapis.com/css2?family=Fira+Sans+Condensed:wght@500;600&family=Montserrat:wght@500&display=swap">
<style>
  :root {
    --stage: #48494b;
    --banner-border: #b9bbbe;
    --banner-top: #ffffff;
    --banner-bottom: #c8cacd;
    --brand-blue: #1d6590;
    --link-blue: #1f6a9e;
    --muted-grey: #5b5d60;
    --tile-border: #9fa2a6;
    --tile-bg: #ffffff;
    --tile-active-bg: #e2f3f7;
    --active-orange: #b4561e;
    --star-tone: #7fc6dc;
    --fish-tone-a: #e9c7a4;
    --fish-tone-b: #5aaee6;
    --top-tone-a: #f7a3c9;
    --top-tone-b: #6fb8ef;
    --top-tone-c: #4dc05a;
  }
  * { box-sizing: border-box; margin: 0; padding: 0; }
  html, body { width: 1200px; height: 900px; overflow: hidden; }
  body { background: var(--stage); position: relative; font-family: "Fira Sans Condensed", "Arial Narrow", sans-serif; }

  .banner {
    position: absolute; top: 262px; width: 450px; height: 375px;
    border: 1px solid var(--banner-border);
    background: linear-gradient(to bottom, var(--banner-top) 0, var(--banner-top) 62%, var(--banner-bottom) 100%);
  }
  .banner--default { left: 133px; }
  .banner--hover { left: 627px; }

  .banner__logo {
    position: absolute; left: 19px; top: 16px;
    font-family: "Montserrat", sans-serif; font-weight: 500;
    font-size: 46px; letter-spacing: 0.5px; color: var(--brand-blue);
  }

  .product { position: absolute; top: 94px; width: 136px; text-align: center; text-decoration: none; }
  .product:nth-of-type(1) { left: 10px; }
  .product:nth-of-type(2) { left: 156px; }
  .product:nth-of-type(3) { left: 304px; }

  .product__tile {
    width: 136px; height: 137px; border: 1px solid var(--tile-border);
    background: var(--tile-bg); display: flex; align-items: center; justify-content: center;
  }
  .product__art { width: 100px; height: 88px; border-radius: 44px; }
  .product__art--star { background: var(--star-tone); width: 92px; border-radius: 30px; }
  .product__art--fish { background: linear-gradient(to right, var(--fish-tone-a) 0 45%, var(--fish-tone-b) 45%); height: 64px; border-radius: 32px; }
  .product__art--top { background: linear-gradient(to bottom, var(--top-tone-a) 0 35%, var(--top-tone-b) 35% 65%, var(--top-tone-c) 65%); width: 90px; height: 84px; }

  .product__name {
    margin-top: 18px; font-weight: 500; font-size: 20px; line-height: 24px; color: var(--link-blue);
  }
  .product--active .product__tile { background: var(--tile-active-bg); }
  .product--active .product__name { color: var(--active-orange); }

  .banner__footer {
    position: absolute; left: 0; right: 0; bottom: 14px; text-align: center;
    font-weight: 600; font-size: 22px; color: var(--muted-grey); word-spacing: 1px;
  }
  .banner__url { color: var(--link-blue); margin-left: 10px; }
</style>
</head>
<body>
  <section class="banner banner--default">
    <div class="banner__logo">Logo</div>
    <a class="product" href="#">
      <div class="product__tile"><div class="product__art product__art--star" role="img" aria-label="Smiling starfish toy illustration"></div></div>
      <div class="product__name">Product<br>Name here</div>
    </a>
    <a class="product" href="#">
      <div class="product__tile"><div class="product__art product__art--fish" role="img" aria-label="Striped toy fish illustration"></div></div>
      <div class="product__name">Product<br>Name here</div>
    </a>
    <a class="product" href="#">
      <div class="product__tile"><div class="product__art product__art--top" role="img" aria-label="Colourful spinning top illustration"></div></div>
      <div class="product__name">Product<br>Name here</div>
    </a>
    <div class="banner__footer">See examples on <span class="banner__url">www.example.com</span></div>
  </section>

  <section class="banner banner--hover">
    <div class="banner__logo">Logo</div>
    <a class="product" href="#">
      <div class="product__tile"><div class="product__art product__art--star" role="img" aria-label="Smiling starfish toy illustration"></div></div>
      <div class="product__name">Product<br>Name here</div>
    </a>
    <a class="product product--active" href="#">
      <div class="product__tile"><div class="product__art product__art--fish" role="img" aria-label="Striped toy fish illustration"></div></div>
      <div class="product__name">Product<br>Name here</div>
    </a>
    <a class="product" href="#">
      <div class="product__tile"><div class="product__art product__art--top" role="img" aria-label="Colourful spinning top illustration"></div></div>
      <div class="product__name">Product<br>Name here</div>
    </a>
    <div class="banner__footer">See examples on <span class="banner__url">www.example.com</span></div>
  </section>
</body>
</html>
```